Information Brochure for Nurse Practitioner Clinic

We need a double-sided trifold informational brochure for patients that will be used to advertise a pharmacy-based nurse practitioner clinic. The clinic would best be described as a "Convenience Care and Wellness Clinic". Lanternway Healthcare offers heathcare services for minor health conditions, specialised health screening assessments in lung, heart and travel health, screening and healthcare advice for common health conditions, and advice and assistance with lifestyle modification. The vision for Lanternway Healthcare is to provide patient-centred, safe, effective, integrated, affordable and accessible healthcare that focuses on wellness and prevention strategies using a nursing model of healthcare. The brochure will be used to inform patients about the role of the nurse practitioner, as well as some of the services offered by the clinic. The final design should communicate caring, holistic approach, and professional.

Target Market(s)

Persons going into a pharmacy.

Industry/Entity Type

Healthcare

Font styles to use
Sans Serif

Colors
0355a3
6b449b

Requirements
Must have
• Most information contained on the webpage https://www.lanternwaycare.com.au/clinic should be included. Logos for clinic have been attached.
Nice to have
• The look for the brochure should be clean, professional and, if using imagery of people, should be Australian in appearance. We should see designs that incorporate the blue and/or purple colours in the attached document.
Should not have
• Information from the above mentioned website should be included EXCEPT for the following information contained under the "Questions" section: "Do you bulk bill?", "How much do your services cost", "What can't you do as a nurse practitioner?", "I'm having issues with the Clinofile app", and "I have feedback about the care...".
• Brochure should not be "cute" or involve stereotypical nursing imagery (i.e. female, in uniforms, etc.)

```html
<!DOCTYPE html>
<html lang="en">
<head>
<meta charset="utf-8">
<title>Lanternway Healthcare – Trifold Brochure</title>
<link href="https://fonts.googleapis.com/css2?family=Roboto+Condensed:ital,wght@0,300;0,400;0,700;1,300;1,400&display=swap" rel="stylesheet">
<style>
  :root{
    --blue:#0355a3;
    --blue-deep:#0a3f8f;
    --blue-light:#4aa8e8;
    --purple:#6b449b;
    --white:#ffffff;
    --page:#e9eaec;
    --ink-soft:#e8ecf7;
  }
  *{margin:0;padding:0;box-sizing:border-box}
  html,body{width:1200px;height:1200px;overflow:hidden;background:var(--page)}
  body{font-family:"Roboto Condensed",sans-serif;position:relative}
  .brochure{position:absolute;left:40px;top:165px;width:1120px;height:870px;background:var(--white);box-shadow:0 10px 30px rgba(0,0,0,.25);overflow:hidden}
  .panel{position:absolute;top:0;height:870px;width:373px;overflow:hidden}
  .panel--services{left:0}
  .panel--vision{left:373px;width:374px}
  .panel--cover{left:747px}
  .abs{position:absolute}
  .shape{position:absolute;left:0;top:0;width:100%;height:100%}

  /* services */
  .services__photo{left:0;top:55px;width:373px;height:250px;background:linear-gradient(135deg,#f4f6fa 0%,#dfe7f1 55%,#c9d8ea 100%)}
  .services__title{left:0;width:373px;top:308px;text-align:center;color:var(--white);font-size:29px;line-height:37px;font-weight:400}
  .services__list{list-style:none;left:40px;top:0;width:290px}
  .services__item{position:absolute;left:0;width:290px;color:var(--white);font-size:17.5px;line-height:22px;padding-left:32px;font-weight:300}
  .services__item svg{position:absolute;left:0;top:3px;width:18px;height:16px}

  /* vision */
  .vision__lead{left:0;width:374px;top:36px;text-align:center;color:var(--white);font-size:17px;font-weight:300}
  .vision__lead span{font-size:38px}
  .vision__body{left:52px;width:270px;top:79px;text-align:center;color:var(--ink-soft);font-size:17px;line-height:22px;font-weight:300}
  .vision__body strong{font-weight:700;color:var(--white)}
  .vision__quote{left:22px;width:332px;top:280px;text-align:center;color:var(--white);font-style:italic;font-size:15.5px;line-height:20px;font-weight:300}
  .vision__mark{font-size:30px;font-weight:700;font-style:italic;line-height:0;vertical-align:-6px;color:var(--white)}
  .vision__cite{left:0;width:344px;top:370px;text-align:right;color:var(--white);font-size:10.5px}
  .vision__portrait{left:96px;top:402px;width:190px;height:185px;border-radius:6px 6px 0 0;background:linear-gradient(180deg,#8b6fb4 0%,#3a3f86 100%)}
  .vision__name{left:0;width:374px;top:600px;text-align:center;color:var(--white);font-size:21px;padding-left:40px}
  .vision__creds{left:0;width:374px;top:627px;text-align:center;color:var(--white);font-size:13px;font-weight:300}
  .contact__heading{left:0;width:374px;top:688px;text-align:center;color:var(--purple);font-size:30px;font-weight:700}
  .contact__phone{left:0;width:374px;top:725px;text-align:center;color:var(--blue);font-size:45px;font-weight:700}
  .contact__email{left:0;width:374px;top:780px;text-align:center;color:var(--blue);font-size:19px}
  .contact__web{left:0;width:374px;top:814px;text-align:center;color:var(--purple);font-size:15px;font-weight:700;letter-spacing:4px}

  /* cover */
  .brand{left:0;width:373px;top:95px;text-align:center;color:var(--blue);font-weight:700}
  .brand__name{font-size:42px;letter-spacing:1px;line-height:44px}
  .brand__sub{font-size:16px;letter-spacing:10px;line-height:22px;padding-left:10px}
  .cover__title{left:0;width:373px;top:236px;text-align:center;color:var(--blue);font-size:35px;line-height:42px;font-weight:400}
  .cover__title small{font-size:26px}
  .cover__title strong{color:var(--purple);font-weight:700}
  .cover__glow{left:0;top:700px;width:373px;height:90px;background:radial-gradient(ellipse at 50% 50%,rgba(150,200,255,.35) 0%,rgba(150,200,255,0) 70%)}
  .cover__questions{left:39px;width:300px;top:455px;color:var(--white);font-size:16.5px;line-height:21px;font-weight:300}
  .cover__q{padding-bottom:5px;margin-bottom:6px;border-bottom:1px solid rgba(255,255,255,.35)}
  .cover__q:last-child{border-bottom:0}
  .cover__web{left:39px;width:320px;top:812px;color:var(--white);font-size:15px;font-weight:700;letter-spacing:4.3px}
</style>
</head>
<body>
<main class="brochure">

  <section class="panel panel--services">
    <div class="abs services__photo" role="img" aria-label="Photo of a smiling clinician with stethoscope, colleagues attending a patient behind"></div>
    <svg class="shape" viewBox="0 0 373 870" preserveAspectRatio="none" aria-hidden="true">
      <defs>
        <linearGradient id="servicesBlue" x1="0" y1="0" x2="0" y2="1">
          <stop offset="0" stop-color="#0b57ae"/>
          <stop offset=".6" stop-color="#0355a3"/>
          <stop offset="1" stop-color="#2f8fdc"/>
        </linearGradient>
      </defs>
      <path d="M0 300 Q180 250 373 288 L373 870 L0 870 Z" fill="url(#servicesBlue)"/>
    </svg>
    <h2 class="abs services__title">LANTERNWAY HEALTHCARE<br>OFFERS HEATHCARE<br>SERVICES FOR</h2>
    <ul class="abs services__list">
      <li class="services__item" style="top:442px"><svg viewBox="0 0 18 16"><path d="M1 9 L6 14 L17 2" fill="none" stroke="#fff" stroke-width="3"/></svg>Minor health conditions</li>
      <li class="services__item" style="top:485px"><svg viewBox="0 0 18 16"><path d="M1 9 L6 14 L17 2" fill="none" stroke="#fff" stroke-width="3"/></svg>Specialised health screening assessments in lung</li>
      <li class="services__item" style="top:551px"><svg viewBox="0 0 18 16"><path d="M1 9 L6 14 L17 2" fill="none" stroke="#fff" stroke-width="3"/></svg>Heart and travel health</li>
      <li class="services__item" style="top:594px"><svg viewBox="0 0 18 16"><path d="M1 9 L6 14 L17 2" fill="none" stroke="#fff" stroke-width="3"/></svg>Screening and healthcare advice for common health conditions</li>
      <li class="services__item" style="top:660px"><svg viewBox="0 0 18 16"><path d="M1 9 L6 14 L17 2" fill="none" stroke="#fff" stroke-width="3"/></svg>Advice and assistance with lifestyle modification.</li>
    </ul>
  </section>

  <section class="panel panel--vision">
    <svg class="shape" viewBox="0 0 374 870" preserveAspectRatio="none" aria-hidden="true">
      <defs>
        <linearGradient id="visionPurple" x1="0" y1="0" x2="0" y2="1">
          <stop offset="0" stop-color="#6b449b"/>
          <stop offset=".82" stop-color="#6b449b"/>
          <stop offset="1" stop-color="#1a49a6"/>
        </linearGradient>
      </defs>
      <path d="M0 0 H374 V628 Q187 705 0 628 Z" fill="url(#visionPurple)"/>
    </svg>
    <p class="abs vision__lead">The <span>vision</span> for</p>
    <p class="abs vision__body"><strong>Lanternway Healthcare</strong> is to provide patient-centred, safe, effective, integrated, affordable and accessible healthcare that focuses on wellness and prevention strategies using a nursing model of healthcare.</p>
    <blockquote class="abs vision__quote"><span class="vision__mark">&ldquo;</span> My aim is to promote and facilitate the development of innovative and informed nurse practitioner models of care into the existing Australian primary health care infrastructure. <span class="vision__mark">&rdquo;</span></blockquote>
    <p class="abs vision__cite">Daniel Marsh, Primary Healthcare Nurse Practitioner</p>
    <div class="abs vision__portrait" role="img" aria-label="Portrait photo of the nurse practitioner with stethoscope, arms folded"></div>
    <p class="abs vision__name">Dr Daniel Marsh,</p>
    <p class="abs vision__creds">PhD RN MSN(NP) ANP-BC FACNP.</p>
    <h3 class="abs contact__heading">CONTACT US</h3>
    <p class="abs contact__phone">123 456 789</p>
    <p class="abs contact__email">contactyour@email.com</p>
    <p class="abs contact__web">www.lanternwaycare.com.au</p>
  </section>

  <section class="panel panel--cover">
    <svg class="shape" viewBox="0 0 373 870" preserveAspectRatio="none" aria-hidden="true">
      <defs>
        <linearGradient id="coverBlue" x1="0" y1="0" x2="0" y2="1">
          <stop offset="0" stop-color="#0a4fa8"/>
          <stop offset=".55" stop-color="#0355a3"/>
          <stop offset="1" stop-color="#1f6fd0"/>
        </linearGradient>
      </defs>
      <path d="M0 440 Q186 365 373 440 L373 870 L0 870 Z" fill="url(#coverBlue)"/>
    </svg>
    <div class="abs cover__glow" role="img" aria-label="Soft glowing heartbeat line decoration"></div>
    <div class="abs brand">
      <div class="brand__name">LANTERNWAY</div>
      <div class="brand__sub">HEALTHCARE</div>
    </div>
    <h1 class="abs cover__title">CONVENIENCE<br>CARE <small>AND</small><br><strong>WELLNESS CLINIC</strong></h1>
    <div class="abs cover__questions">
      <p class="cover__q">Do you feel you've had a comprehensive, head-to-toe health assessment recently?</p>
      <p class="cover__q">Do you feel you have ownership of your long-term health condition?</p>
      <p class="cover__q">Do you feel empowered to make decisions impacting upon your health?</p>
      <p class="cover__q">Come in for your bulk-billed initial assessment to help you find the answers to your health-care needs.</p>
    </div>
    <p class="abs cover__web">www.lanternwaycare.com.au</p>
  </section>

</main>
</body>
</html>
```